Email Signature & Facebook Cover Design – Brightpath Learning Nook

I’m looking for a clean, professional email signature and a matching Facebook cover photo for my tutoring business, Brightpath Learning Nook.
The email signature needs to display properly across Outlook and iPhone without the image appearing as an attachment. It should include my logo and contact details and have a friendly but professional look suitable for an education business.
Details to include:
Dana Morrow
Director & Lead Tutor
Brightpath Learning Nook
hello@brightpathlearningnook.co.uk
www.brightpathlearningnook.co.uk
01632 960418
The Facebook cover should match the branding, feel professional and welcoming, and be optimised for desktop and mobile.

```html
<!DOCTYPE html>
<html lang="en">
<head>
<meta charset="utf-8">
<title>Brightpath Learning Nook – Facebook Cover &amp; Email Signature</title>
<link rel="stylesheet" href="https://fonts.googleapis.com/css2?family=Poppins:ital,wght@0,400;0,600;0,700;1,400&display=swap">
<style>
  :root {
    --board: #e6e6e6;
    --green: #47ae64;
    --green-dark: #2b944d;
    --lime: #c3fa62;
    --white: #ffffff;
  }
  * { margin: 0; padding: 0; box-sizing: border-box; }
  html, body { width: 1200px; height: 876px; overflow: hidden; }
  body {
    position: relative;
    background: var(--board);
    font-family: "Poppins", sans-serif;
    color: var(--white);
  }

  .cover {
    position: absolute; left: 72px; top: 51px; width: 1043px; height: 385px;
    background: var(--green); overflow: hidden;
  }
  .rings { position: absolute; inset: 0; }
  .cover-headline {
    position: absolute; left: 74px; top: 92px;
    font-size: 33px; font-weight: 400; line-height: 40px; letter-spacing: 0.2px;
  }
  .cover-headline strong { color: var(--lime); font-weight: 700; }
  .cover-wordmark {
    position: absolute; left: 267px; top: 262px;
    color: var(--lime); font-weight: 700; font-size: 27px; line-height: 31px;
  }
  .brain-art {
    position: absolute; left: 532px; top: 18px; width: 501px; height: 367px;
    border-radius: 50% 50% 0 0 / 40% 40% 0 0;
    background: radial-gradient(ellipse at 50% 30%, #7fcf5e 0%, #3a9f55 45%, var(--green-dark) 70%);
  }

  .profile-badge {
    position: absolute; left: 102px; top: 310px; width: 207px; height: 205px;
    background: var(--green); border: 8px solid var(--white);
    display: flex; align-items: center; justify-content: center; text-align: center;
    color: var(--lime); font-weight: 700; font-size: 26px; line-height: 31px;
  }

  .signature {
    position: absolute; left: 259px; top: 553px; width: 723px; height: 238px;
    background: var(--green); overflow: hidden;
  }
  .sig-logo {
    position: absolute; left: 37px; top: 34px; width: 170px; height: 170px;
    border-radius: 50%; background: var(--green); border: 6px solid var(--white);
    display: flex; align-items: center; justify-content: center; text-align: center;
    font-weight: 700; font-size: 19px; line-height: 23px; color: var(--white);
  }
  .sig-details { position: absolute; left: 235px; top: 32px; z-index: 2; }
  .sig-name { color: var(--lime); font-weight: 700; font-size: 20px; line-height: 28px; }
  .sig-role { font-style: italic; font-size: 14px; line-height: 22px; }
  .sig-company { font-weight: 700; font-size: 20px; line-height: 28px; }
  .sig-contacts { list-style: none; margin-top: 17px; }
  .sig-contacts li {
    display: flex; align-items: center; gap: 9px;
    font-size: 15px; line-height: 25px; white-space: nowrap;
  }
  .contact-icon { width: 17px; height: 17px; flex: none; }
  .sig-brain-art {
    position: absolute; left: 562px; top: 67px; width: 161px; height: 171px;
    border-radius: 50% 50% 0 0 / 45% 45% 0 0;
    background: radial-gradient(ellipse at 50% 30%, #7fcf5e 0%, #3a9f55 45%, var(--green-dark) 72%);
  }
</style>
</head>
<body>

<section class="cover" aria-label="Facebook cover">
  <svg class="rings" width="1043" height="385" aria-hidden="true">
    <circle cx="18" cy="13" r="166" fill="none" stroke="var(--green-dark)" stroke-width="68"/>
    <circle cx="272" cy="378" r="153" fill="none" stroke="var(--green-dark)" stroke-width="43"/>
  </svg>
  <h1 class="cover-headline">Learning that clicks,<br><strong>Confidence</strong> that truly<br>sticks.</h1>
  <div class="cover-wordmark">Brightpath<br>Learning<br>Nook</div>
  <div class="brain-art" role="img" aria-label="Illustration of two head silhouettes back to back, one brain drawn as a circuit board and one as a natural brain"></div>
</section>

<div class="profile-badge">Brightpath<br>Learning<br>Nook</div>

<section class="signature" aria-label="Email signature">
  <svg class="rings" width="723" height="238" aria-hidden="true">
    <circle cx="6" cy="-23" r="224" fill="none" stroke="var(--green-dark)" stroke-width="46"/>
    <circle cx="652" cy="-23" r="106" fill="none" stroke="var(--green-dark)" stroke-width="32"/>
  </svg>
  <div class="sig-brain-art" role="img" aria-label="Small illustration of two head silhouettes with circuit-board and natural brains"></div>
  <div class="sig-logo">Brightpath<br>Learning<br>Nook</div>
  <div class="sig-details">
    <p class="sig-name">Dana Morrow</p>
    <p class="sig-role">Director &amp; Lead Tutor</p>
    <p class="sig-company">Brightpath Learning Nook</p>
    <ul class="sig-contacts">
      <li>
        <svg class="contact-icon" viewBox="0 0 18 18" aria-hidden="true"><circle cx="9" cy="9" r="9" fill="var(--lime)"/><path d="M6 4.5l2 2-1 1.2c.6 1.3 1.6 2.3 2.9 2.9l1.2-1 2 2-1.2 1.4C9 12.8 5.2 9 4.6 5.7z" fill="var(--green)"/></svg>
        01632 960418
      </li>
      <li>
        <svg class="contact-icon" viewBox="0 0 18 18" aria-hidden="true"><circle cx="9" cy="9" r="9" fill="var(--lime)"/><rect x="4.5" y="5.5" width="9" height="7" rx="1" fill="var(--green)"/><path d="M4.8 6l4.2 3.4L13.2 6" fill="none" stroke="var(--lime)" stroke-width="1"/></svg>
        hello@brightpathlearningnook.co.uk
      </li>
      <li>
        <svg class="contact-icon" viewBox="0 0 18 18" aria-hidden="true"><circle cx="9" cy="9" r="9" fill="var(--lime)"/><g fill="none" stroke="var(--green)" stroke-width="1"><circle cx="9" cy="9" r="5"/><ellipse cx="9" cy="9" rx="2.2" ry="5"/><path d="M4 9h10M5 6.5h8M5 11.5h8"/></g></svg>
        www.brightpathlearningnook.co.uk
      </li>
    </ul>
  </div>
</section>

</body>
</html>
```